Innovative Freezer Label Design

Create a versatile and innovative freezer label design with universal appeal, suitable for different functionalities. The design should cater to a diverse audience, including those who freeze meals for meal prepping, batch cooking, and the restaurant industry. Our vision is a visually striking and distinctive design that embodies simplicity.

Example "our current labels feature essential details like "Contents" and "Date." We recognize these as crucial points of information. Currently, the challenge lies in creating various labels for different marketplaces, considering language barriers. A proposed solution involves the integration of universal icons to replace specific words, promoting practicality for international sales."

Kindly note that design concepts should not be restricted to our current product, brand guideline, logo, or the provided example.

Our goal is not only product differentiation but also increased sales through a blend of functionality and aesthetics.

The following are examples of freezer labels designs. Kindly do not restrict your designs to the examples. The designs must be universal (for language barrier purposes)

Examples:
https://www.tackvora.co.uk/pin/5827164039281736401/
https://www.tackvora.co.uk/pin/5827164039281736405/
https://www.tackvora.co.uk/pin/5827164039281736394/
https://www.tackvora.co.uk/pin/5827164039281736308/
https://www.tackvora.co.uk/pin/5827164039281797750/

Please reach out if you have any questions.

Thank you

```html
<!DOCTYPE html>
<html lang="en">
<head>
<meta charset="utf-8">
<title>Brindle Eco – Freezer Labels</title>
<link rel="stylesheet" href="https://fonts.googleapis.com/css2?family=EB+Garamond:wght@500;600&display=swap">
<style>
  :root {
    --page: #ffffff;
    --red-ink: #a84b50;
    --red-paper: #ecd6cc;
    --navy-ink: #364b5e;
    --navy-paper: #c9cbd3;
    --green-ink: #4a6b5a;
    --green-paper: #d3ddd7;
  }
  * { margin: 0; padding: 0; box-sizing: border-box; }
  html, body {
    width: 1200px;
    height: 1200px;
    overflow: hidden;
    background: var(--page);
  }
  .sheet {
    position: relative;
    width: 1200px;
    height: 1200px;
  }
  .label {
    position: absolute;
    left: 307px;
    width: 574px;
    height: 356px;
    border-radius: 14px;
    overflow: hidden;
    background: var(--ink);
  }
  .label--red   { top: 46px;  --ink: var(--red-ink);   --paper: var(--red-paper); }
  .label--navy  { top: 430px; --ink: var(--navy-ink);  --paper: var(--navy-paper); }
  .label--green { top: 817px; --ink: var(--green-ink); --paper: var(--green-paper); }

  .label__panel {
    position: absolute;
    left: 0;
    top: 22px;
    width: 100%;
    height: 280px;
    background: var(--paper);
    border-radius: 10px;
  }
  .label__pattern {
    position: absolute;
    left: 0;
    bottom: 0;
    width: 100%;
    height: 54px;
    background: var(--ink);
  }
  .label__brand {
    position: absolute;
    top: 44px;
    left: 0;
    width: 100%;
    text-align: center;
    font-family: "EB Garamond", Georgia, serif;
    font-weight: 600;
    font-size: 34px;
    letter-spacing: 1.5px;
    color: var(--ink);
    line-height: 1;
  }
  .label__line {
    position: absolute;
    left: 99px;
    width: 388px;
    height: 2px;
    background: var(--ink);
  }
  .label__line--contents { top: 120px; }
  .label__line--extra    { top: 201px; }

  .label__date-icon {
    position: absolute;
    left: 99px;
    top: 220px;
    width: 64px;
    height: 64px;
    color: var(--ink);
  }
  .label__date-slash {
    position: absolute;
    top: 230px;
    font-family: "EB Garamond", Georgia, serif;
    font-weight: 500;
    font-size: 44px;
    line-height: 1;
    color: var(--ink);
  }
  .label__date-slash--first  { left: 276px; }
  .label__date-slash--second { left: 357px; }
</style>
</head>
<body>
<main class="sheet">

  <section class="label label--red">
    <div class="label__panel"></div>
    <div class="label__pattern" role="img" aria-label="Red marble texture band with pale veining"></div>
    <p class="label__brand">Brindle Eco</p>
    <div class="label__line label__line--contents"></div>
    <div class="label__line label__line--extra"></div>
    <svg class="label__date-icon" viewBox="0 0 64 64" fill="none" stroke="currentColor" stroke-width="2.2" aria-label="Date">
      <rect x="4" y="9" width="56" height="51" rx="4"/>
      <line x1="4" y1="20" x2="60" y2="20"/>
      <line x1="18" y1="4" x2="18" y2="14"/>
      <line x1="46" y1="4" x2="46" y2="14"/>
      <g>
        <circle cx="16" cy="29" r="3"/><circle cx="27" cy="29" r="3"/><circle cx="38" cy="29" r="3"/><circle cx="49" cy="29" r="3"/>
        <circle cx="16" cy="39" r="3"/><circle cx="27" cy="39" r="3"/><circle cx="38" cy="39" r="3"/><circle cx="49" cy="39" r="3"/>
        <circle cx="16" cy="49" r="3"/><circle cx="27" cy="49" r="3"/><circle cx="38" cy="49" r="3"/><circle cx="49" cy="49" r="3"/>
      </g>
    </svg>
    <span class="label__date-slash label__date-slash--first">/</span>
    <span class="label__date-slash label__date-slash--second">/</span>
  </section>

  <section class="label label--navy">
    <div class="label__panel"></div>
    <div class="label__pattern" role="img" aria-label="Navy band with pale wave pattern"></div>
    <p class="label__brand">Brindle Eco</p>
    <div class="label__line label__line--contents"></div>
    <div class="label__line label__line--extra"></div>
    <svg class="label__date-icon" viewBox="0 0 64 64" fill="none" stroke="currentColor" stroke-width="2.2" aria-label="Date">
      <rect x="4" y="9" width="56" height="51" rx="4"/>
      <line x1="4" y1="20" x2="60" y2="20"/>
      <line x1="18" y1="4" x2="18" y2="14"/>
      <line x1="46" y1="4" x2="46" y2="14"/>
      <g>
        <circle cx="16" cy="29" r="3"/><circle cx="27" cy="29" r="3"/><circle cx="38" cy="29" r="3"/><circle cx="49" cy="29" r="3"/>
        <circle cx="16" cy="39" r="3"/><circle cx="27" cy="39" r="3"/><circle cx="38" cy="39" r="3"/><circle cx="49" cy="39" r="3"/>
        <circle cx="16" cy="49" r="3"/><circle cx="27" cy="49" r="3"/><circle cx="38" cy="49" r="3"/><circle cx="49" cy="49" r="3"/>
      </g>
    </svg>
    <span class="label__date-slash label__date-slash--first">/</span>
    <span class="label__date-slash label__date-slash--second">/</span>
  </section>

  <section class="label label--green">
    <div class="label__panel"></div>
    <div class="label__pattern" role="img" aria-label="Green band with pale outlined leaf pattern"></div>
    <p class="label__brand">Brindle Eco</p>
    <div class="label__line label__line--contents"></div>
    <div class="label__line label__line--extra"></div>
    <svg class="label__date-icon" viewBox="0 0 64 64" fill="none" stroke="currentColor" stroke-width="2.2" aria-label="Date">
      <rect x="4" y="9" width="56" height="51" rx="4"/>
      <line x1="4" y1="20" x2="60" y2="20"/>
      <line x1="18" y1="4" x2="18" y2="14"/>
      <line x1="46" y1="4" x2="46" y2="14"/>
      <g>
        <circle cx="16" cy="29" r="3"/><circle cx="27" cy="29" r="3"/><circle cx="38" cy="29" r="3"/><circle cx="49" cy="29" r="3"/>
        <circle cx="16" cy="39" r="3"/><circle cx="27" cy="39" r="3"/><circle cx="38" cy="39" r="3"/><circle cx="49" cy="39" r="3"/>
        <circle cx="16" cy="49" r="3"/><circle cx="27" cy="49" r="3"/><circle cx="38" cy="49" r="3"/><circle cx="49" cy="49" r="3"/>
      </g>
    </svg>
    <span class="label__date-slash label__date-slash--first">/</span>
    <span class="label__date-slash label__date-slash--second">/</span>
  </section>

</main>
</body>
</html>
```